Law Firm Needs a Stationery Design

We need a stationery design for a law firm based in the East African region called 'Mbweteka Olinyo & Company Advocates'. We are a law firm specializing in commercial, public and constitutional law. Our practice areas include Telecommunications Law, Mining Law, Oil and Energy Law, Real Estate and Land Development Law, Employment Law, Family Law, Civil and Criminal Litigation, Constitutional Law, Company Secretariat and more. We represent a wide variety of clients, ranging from individuals to corporations and approach each case with full attention, dedication and legal acumen in order to protect the interests of our clients. The final stationary design should communicate innovation and expertise to meet our clients’ legal needs.
Target Market(s)
New clients, current and former clients, other lawyers in and outside of our practice area, or other professionals, contacts and centers of influence within the region
Industry/Entity Type
Real Estate
Colors
Designer to choose colors to be used in the design.
Look and feel
Each slider illustrates characteristics of the customer's brand and the style your logo design should communicate.

```html
<!DOCTYPE html>
<html lang="en">
<head>
<meta charset="utf-8">
<title>Mbweteka Olinyo &amp; Company Advocates — Stationery</title>
<link href="https://fonts.googleapis.com/css2?family=Cinzel:wght@500&family=Open+Sans:wght@400;600;700&display=swap" rel="stylesheet">
<style>
  :root {
    --navy: #1c3466;
    --navy-dark: #142750;
    --grey: #8c9099;
    --grey-light: #c9ccd2;
    --paper: #fbfbfb;
    --ground: #eceef1;
    --ink: #3d4046;
  }
  * { box-sizing: border-box; margin: 0; padding: 0; }
  html, body { width: 1200px; height: 550px; overflow: hidden; }
  body {
    background: var(--ground);
    font-family: "Open Sans", Arial, sans-serif;
    color: var(--ink);
    position: relative;
  }
  .sheet {
    position: absolute;
    background: var(--paper);
    box-shadow: 0 1px 4px rgba(0,0,0,.12);
    overflow: hidden;
  }
  .wordmark {
    display: flex; align-items: center; gap: 5px;
    font-family: "Cinzel", Georgia, serif; font-weight: 500;
    color: var(--navy); line-height: 1.05;
  }
  .wordmark .mark-square { background: var(--navy); flex: none; }
  .wordmark.on-navy { color: #fff; }
  .band { position: absolute; left: 0; right: 0; bottom: 0; }
  .band .rule { height: 1px; background: var(--grey-light); }
  .band .bar { background: var(--navy); }
  .icon { width: 5px; height: 5px; fill: var(--navy); flex: none; }
  .contact-row { display: flex; align-items: center; gap: 3px; }

  /* business card front */
  .card-front { left: 75px; top: 40px; width: 152px; height: 87px; }
  .card-front .wordmark { position: absolute; left: 9px; top: 12px; font-size: 5.3px; }
  .card-front .wordmark .mark-square { width: 13px; height: 13px; }
  .card-front .holder { position: absolute; right: 10px; top: 41px; text-align: right; }
  .card-front .holder-name { font-size: 5px; font-weight: 700; color: var(--navy); }
  .card-front .holder-role { font-size: 3.4px; color: var(--grey); }
  .card-front .divider { position: absolute; left: 9px; right: 9px; top: 55px; height: 1px; background: var(--grey-light); }
  .card-front .contacts { position: absolute; left: 9px; top: 60px; font-size: 3.6px; line-height: 5.4px; }
  .card-front .address { position: absolute; right: 10px; top: 60px; font-size: 3.6px; line-height: 5.4px; text-align: right; }
  .card-front .band .bar { height: 3px; }

  /* business card back */
  .card-back {
    left: 243px; top: 40px; width: 151px; height: 87px;
    background: radial-gradient(ellipse at 50% 35%, #2a4785 0%, var(--navy) 55%, var(--navy-dark) 100%);
    display: flex; flex-direction: column; align-items: center; justify-content: center; gap: 9px;
  }
  .card-back .wordmark { font-size: 6.5px; text-align: center; }
  .card-back .web { font-size: 3.8px; color: #dfe4ee; }

  /* envelope front */
  .envelope-front { left: 47px; top: 148px; width: 373px; height: 178px; }
  .envelope-front .wordmark { position: absolute; left: 20px; top: 24px; font-size: 8.5px; }
  .envelope-front .wordmark .mark-square { width: 20px; height: 20px; }
  .envelope-front .address { position: absolute; left: 20px; top: 62px; font-size: 5px; color: var(--grey); }
  .envelope-front .window {
    position: absolute; left: 20px; top: 74px; width: 147px; height: 41px;
    border-radius: 6px; background: #f0f1f2; border: 1px solid #e2e4e7;
  }
  .envelope-front .band { bottom: 16px; }
  .envelope-front .band .bar { height: 7px; }

  /* envelope back */
  .envelope-back { left: 47px; top: 334px; width: 373px; height: 178px; }
  .envelope-back .flap { position: absolute; left: 0; top: 0; width: 100%; height: 70px; }
  .envelope-back .wordmark {
    position: absolute; left: 0; right: 0; top: 22px;
    justify-content: center; font-size: 8px; text-align: center;
  }

  /* letterhead */
  .letterhead { left: 439px; top: 41px; width: 332px; height: 473px; }
  .letterhead .wordmark { position: absolute; left: 0; right: 0; top: 30px; justify-content: center; font-size: 9px; }
  .letterhead .wordmark .mark-square { width: 22px; height: 22px; }
  .letterhead .date { position: absolute; left: 40px; top: 131px; font-size: 5.5px; color: var(--ink); }
  .letterhead .subject { position: absolute; left: 40px; top: 141px; font-size: 8.5px; font-weight: 700; letter-spacing: 1.2px; color: var(--navy); }
  .letterhead .body { position: absolute; left: 40px; width: 252px; font-size: 4.6px; line-height: 8.6px; font-weight: 600; color: #4e5158; text-align: justify; }
  .letterhead .body.p1 { top: 165px; }
  .letterhead .body.p2 { top: 223px; }
  .letterhead .body.p3 { top: 306px; }
  .letterhead .seal { position: absolute; left: 36px; top: 333px; width: 60px; height: 60px; }
  .letterhead .footer {
    position: absolute; left: 0; right: 0; bottom: 14px;
    display: flex; justify-content: center; gap: 6px;
    font-size: 4.2px; color: var(--ink);
  }
  .letterhead .band .bar { height: 8px; }

  /* seal on desk surface */
  .standalone-seal { position: absolute; left: 889px; top: 189px; width: 71px; height: 71px; }

  /* compliment slip */
  .compliment-slip { left: 788px; top: 334px; width: 373px; height: 178px; }
  .compliment-slip .wordmark { position: absolute; left: 21px; top: 23px; font-size: 8px; }
  .compliment-slip .wordmark .mark-square { width: 20px; height: 20px; }
  .compliment-slip .greeting {
    position: absolute; right: 24px; top: 26px;
    font-family: "Cinzel", Georgia, serif; font-weight: 500; font-size: 6.6px;
    letter-spacing: .5px; color: var(--navy);
  }
  .compliment-slip .holder { position: absolute; left: 21px; top: 102px; font-size: 5.4px; line-height: 8px; }
  .compliment-slip .holder-name { font-weight: 700; color: var(--navy); font-size: 6px; line-height: 7px; }
  .compliment-slip .holder-role { font-size: 3.8px; color: var(--grey); line-height: 7px; }
  .compliment-slip .band { bottom: 0; }
  .compliment-slip .band .bar { height: 7px; }
</style>
</head>
<body>

<svg width="0" height="0" style="position:absolute">
  <defs>
    <symbol id="icon-phone" viewBox="0 0 10 10"><path d="M2 1h2l1 2.4-1.3.9a6 6 0 0 0 2 2l.9-1.3L9 6v2a1 1 0 0 1-1 1A8 8 0 0 1 1 2a1 1 0 0 1 1-1z"/></symbol>
    <symbol id="icon-mail" viewBox="0 0 10 10"><circle cx="5" cy="5" r="4.5"/><circle cx="5" cy="5" r="2" fill="#fff"/></symbol>
    <symbol id="icon-web" viewBox="0 0 10 10"><circle cx="5" cy="5" r="4.5"/><path d="M.5 5h9M5 .5v9" stroke="#fff" stroke-width=".9"/></symbol>
  </defs>
</svg>

<!-- Business card, front -->
<section class="sheet card-front">
  <div class="wordmark"><span class="mark-square"></span><span>Mbweteka Olinyo<br>&amp; Company Advocates</span></div>
  <div class="holder">
    <div class="holder-name">Peter Amani</div>
    <div class="holder-role">Attorney</div>
  </div>
  <div class="divider"></div>
  <div class="contacts">
    <div class="contact-row"><svg class="icon"><use href="#icon-phone"/></svg>+256 300 418 552</div>
    <div class="contact-row"><svg class="icon"><use href="#icon-mail"/></svg>peter@mbwetekaolinyo.com</div>
    <div class="contact-row"><svg class="icon"><use href="#icon-web"/></svg>www.mbwetekaolinyo.com</div>
  </div>
  <div class="address">Plot 7-9 Nsambya Lane<br>Kisugu, Kampala, Uganda</div>
  <div class="band"><div class="rule"></div><div class="bar"></div></div>
</section>

<!-- Business card, back -->
<section class="sheet card-back">
  <div class="wordmark on-navy"><span>Mbweteka Olinyo<br>&amp; Company Advocates</span></div>
  <div class="web">www.mbwetekaolinyo.com</div>
</section>

<!-- Envelope, front -->
<section class="sheet envelope-front">
  <div class="wordmark"><span class="mark-square"></span><span>Mbweteka Olinyo<br>&amp; Company Advocates</span></div>
  <div class="address">Plot 7-9 Nsambya Lane, Kisugu, Kampala, Uganda</div>
  <div class="window"></div>
  <div class="band"><div class="rule"></div><div class="bar"></div></div>
</section>

<!-- Envelope, back -->
<section class="sheet envelope-back">
  <svg class="flap" viewBox="0 0 373 70" preserveAspectRatio="none">
    <path d="M0 0H373V58Q373 68 362 66Q186 52 11 66Q0 68 0 58Z" fill="#1c3466"/>
  </svg>
  <div class="wordmark on-navy"><span>Mbweteka Olinyo<br>&amp; Company Advocates</span></div>
</section>

<!-- Letterhead -->
<section class="sheet letterhead">
  <div class="wordmark"><span class="mark-square"></span><span>Mbweteka Olinyo<br>&amp; Company Advocates</span></div>
  <div class="date">16 . September . 2013</div>
  <div class="subject">SUBJECT:</div>
  <p class="body p1">Lorem ipsum dolor sit amet, consectetur adipisicing elit, sed do eiusmod tempor incididunt ut labore et dolore magna aliqua. Ut enim ad minim veniam, quis nostrud exercitation ullamco laboris nisi ut aliquip ex ea commodo consequat. Duis aute irure dolor in reprehenderit in voluptate velit esse cillum dolore eu fugiat nulla pariatur. Excepteur sint occaecat cupidatat non proident, sunt in culpa qui officia deserunt mollit anim id est laborum.</p>
  <p class="body p2">Sed ut perspiciatis unde omnis iste natus error sit voluptatem accusantium doloremque laudantium, totam rem aperiam, eaque ipsa quae ab illo inventore veritatis et quasi architecto beatae vitae dicta sunt explicabo. Nemo enim ipsam voluptatem quia voluptas sit aspernatur aut odit aut fugit, sed quia consequuntur magni dolores eos qui ratione voluptatem sequi nesciunt. Neque porro quisquam est, qui dolorem ipsum quia dolor sit amet, consectetur, adipisci velit, sed quia non numquam eius modi tempora incidunt ut labore et dolore magnam aliquam quaerat voluptatem. Ut enim ad minima veniam, quis nostrum exercitationem ullam corporis suscipit laboriosam, nisi ut aliquid ex ea commodi consequatur.</p>
  <p class="body p3">Quis autem vel eum iure reprehenderit qui in ea voluptate velit esse quam nihil molestiae consequatur, vel illum qui dolorem eum fugiat quo voluptas nulla pariatur.</p>
  <svg class="seal" viewBox="0 0 60 60" aria-hidden="true">
    <circle cx="30" cy="30" r="28" fill="none" stroke="#2a4785" stroke-width="1.6" opacity=".8"/>
    <circle cx="30" cy="30" r="19" fill="none" stroke="#2a4785" stroke-width=".8" opacity=".8"/>
  </svg>
  <div class="footer">
    <span>Plot 7-9 Nsambya Lane, Kisugu, Kampala, Uganda</span>
    <span class="contact-row"><svg class="icon"><use href="#icon-phone"/></svg>+256 300 418 552</span>
    <span class="contact-row"><svg class="icon"><use href="#icon-mail"/></svg>info@mbwetekaolinyo.com</span>
    <span class="contact-row"><svg class="icon"><use href="#icon-web"/></svg>www.mbwetekaolinyo.com</span>
  </div>
  <div class="band"><div class="rule"></div><div class="bar"></div></div>
</section>

<!-- Seal impression -->
<svg class="standalone-seal" viewBox="0 0 71 71" aria-hidden="true">
  <circle cx="35.5" cy="35.5" r="33.5" fill="none" stroke="#1c3466" stroke-width="1.8"/>
  <circle cx="35.5" cy="35.5" r="30.5" fill="none" stroke="#1c3466" stroke-width=".7"/>
  <circle cx="35.5" cy="35.5" r="21" fill="none" stroke="#1c3466" stroke-width=".9"/>
</svg>

<!-- Compliment slip -->
<section class="sheet compliment-slip">
  <div class="wordmark"><span class="mark-square"></span><span>Mbweteka Olinyo<br>&amp; Company Advocates</span></div>
  <div class="greeting">WITH BEST COMPLIMENT FROM</div>
  <div class="holder">
    <div class="holder-name">Peter Amani</div>
    <div class="holder-role">Attorney</div>
    <div>Plot 7-9 Nsambya Lane</div>
    <div>Kisugu, Kampala, Uganda</div>
    <div class="contact-row"><svg class="icon"><use href="#icon-phone"/></svg>+256 300 418 552</div>
    <div class="contact-row"><svg class="icon"><use href="#icon-mail"/></svg>peter@mbwetekaolinyo.com</div>
    <div class="contact-row"><svg class="icon"><use href="#icon-web"/></svg>www.mbwetekaolinyo.com</div>
  </div>
  <div class="band"><div class="rule"></div><div class="bar"></div></div>
</section>

</body>
</html>
```